Aspiring new agent needs for sale signs for real estate :D

I need a for sale sign that is branding myself as I will be a solo agent here soon. If I like it, I will also decides to get business cards made as well as other images for my business. I want to keep it all cohesive and similar so my branding doesn't jump around.

I'm looking for a design that I can have printed as a for sale sigh on my real estate listings. Must say FOR SALE at the top. Be a vertically oriented rectangle, have Mina Todrow Realtor 555-418-7731 on it. It will also need space saved for the Harlow Penfield logo at the bottom and disclosure on it but I will provide that once I've found the design I'm in favor of. I like light colors, but because of the brokerage I'm in, it needs some red in the design. I also want the picture of myself provided on the design. Thank you :)

Industry/Entity Type

Real Estate Agent

Logo Text

Mina Todrow Real estate 555-418-7730 HP Alaska Group, Harlow Penfield Realty, Each office is independently owned and operated

Logo styles of interest
Abstract Logo
Wordmark Logo
Requirements
Must have
• For Sale sign posted at top. Mina Todrow Realtor. The picture I provided. I also need red in there as the brokerage I work for uses those colors. I like light colors as well, and white.

```html
<!DOCTYPE html>
<html lang="en">
<head>
<meta charset="utf-8">
<title>Mina Todrow Realtor – For Sale Sign</title>
<link href="https://fonts.googleapis.com/css2?family=Montserrat:wght@300;800&family=Lexend:wght@300&display=swap" rel="stylesheet">
<style>
  :root {
    --brand-red: #ae1c27;
    --lime: #b2d33c;
    --teal: #1c9bbd;
    --teal-line: #27a8c6;
    --panel-grey: #e6e7ec;
    --ink: #111111;
    --white: #ffffff;
  }
  html, body {
    margin: 0;
    padding: 0;
    overflow: hidden;
    background: var(--white);
  }
  .sign {
    position: relative;
    width: 851px;
    height: 1200px;
    overflow: hidden;
    background: var(--white);
    font-family: "Montserrat", sans-serif;
  }
  .header-band {
    position: absolute;
    left: 0; top: 0;
    width: 851px; height: 348px;
    background: var(--brand-red);
  }
  .header-frame {
    position: absolute;
    left: 0; top: 0;
  }
  .headline {
    position: absolute;
    left: 0; top: 122px;
    width: 851px;
    margin: 0;
    text-align: center;
    font-family: "Montserrat", sans-serif;
    font-weight: 300;
    font-size: 97px;
    line-height: 1;
    letter-spacing: 22px;
    word-spacing: 30px;
    color: var(--lime);
    text-indent: 8px;
  }
  .agent-photo {
    position: absolute;
    left: 0; top: 348px;
    width: 379px; height: 562px;
    background: linear-gradient(160deg, #8c8a6e 0%, #5c4a3c 35%, #e9dcd8 75%, #f4e6e8 100%);
  }
  .brand-panel {
    position: absolute;
    left: 379px; top: 348px;
    width: 472px; height: 562px;
    background: var(--panel-grey);
  }
  .corner-accent {
    position: absolute;
  }
  .brand-mark {
    position: absolute;
    left: 576px; top: 540px;
    width: 64px; height: 64px;
    background: var(--teal);
  }
  .agent-name {
    position: absolute;
    left: 379px; top: 656px;
    width: 472px;
    margin: 0;
    text-align: center;
    font-weight: 800;
    font-size: 40px;
    line-height: 1;
    letter-spacing: 0.5px;
    color: var(--ink);
  }
  .agent-title {
    position: absolute;
    left: 379px; top: 706px;
    width: 472px;
    margin: 0;
    text-align: center;
    font-family: "Lexend", sans-serif;
    font-weight: 300;
    font-size: 17px;
    line-height: 1;
    letter-spacing: 18px;
    text-indent: 18px;
    color: var(--ink);
  }
  .lime-band {
    position: absolute;
    left: 0; top: 910px;
    width: 851px; height: 17px;
    background: var(--lime);
  }
  .phone {
    position: absolute;
    left: 0; top: 948px;
    width: 851px;
    margin: 0;
    text-align: center;
    font-weight: 800;
    font-size: 58px;
    line-height: 1;
    letter-spacing: 1px;
    color: var(--teal);
  }
  .teal-rule {
    position: absolute;
    left: 0; top: 1028px;
    width: 851px; height: 16px;
    background: var(--teal-line);
  }
  .brokerage-slot {
    position: absolute;
    left: 173px; top: 1067px;
    width: 497px; height: 79px;
    background: var(--brand-red);
  }
  .disclosure {
    position: absolute;
    left: 0; top: 1168px;
    width: 851px;
    margin: 0;
    text-align: center;
    font-family: "Lexend", sans-serif;
    font-weight: 300;
    font-size: 17px;
    line-height: 1;
    color: var(--ink);
  }
</style>
</head>
<body>
<main class="sign">
  <div class="header-band"></div>
  <svg class="header-frame" width="851" height="348" viewBox="0 0 851 348" aria-hidden="true">
    <polyline points="717,38 33,38 33,306 808,306 808,97" fill="none" stroke="#b2d33c" stroke-width="2"/>
    <polygon points="717,37 810,37 810,97" fill="#b2d33c"/>
  </svg>
  <h1 class="headline">FOR SALE</h1>

  <div class="agent-photo" role="img" aria-label="Portrait photo of the agent smiling in a doorway"></div>
  <section class="brand-panel"></section>
  <svg class="corner-accent" style="left:761px;top:348px" width="90" height="60" viewBox="0 0 90 60" aria-hidden="true">
    <polygon points="0,0 90,0 90,60" fill="#b2d33c"/>
  </svg>
  <div class="brand-mark" aria-hidden="true"></div>
  <h2 class="agent-name">MINA TODROW</h2>
  <p class="agent-title">REALTOR</p>

  <div class="lime-band"></div>
  <svg class="corner-accent" style="left:758px;top:927px" width="93" height="60" viewBox="0 0 93 60" aria-hidden="true">
    <polygon points="0,0 93,0 93,60" fill="#b2d33c"/>
  </svg>
  <p class="phone">555-418-7730</p>
  <div class="teal-rule"></div>

  <div class="brokerage-slot" aria-label="Brokerage logo area"></div>
  <p class="disclosure">Each office is independently owned and operated</p>
</main>
</body>
</html>
```